Banner

Hi,
Looking for 6 tiles. 1080 by 1080, we want the angular shapes you've used for us in the past similar to the example but bold and simple design.

Tile 1
Cedar Loop Logo (the books)
include some shapes, bold and simple

Tile 2
Text-
Let Cedar ideas grow
add some shapes

Tile 3
a diagonal line down
on one side have the Cedar Loop Logo (the books) the other side have some shapes

Tile 4
Text-
Let Cedar ideas grow
have a diagonal line down
on one side have add some shapes on the other side

Tile 5
include the rocket from the Tandem logo

Tile 6
Text-
Let Cedar ideas grow

```html
<!DOCTYPE html>
<html lang="en">
<head>
<meta charset="utf-8">
<title>Let Cedar ideas grow</title>
<link rel="stylesheet" href="https://fonts.googleapis.com/css2?family=Montserrat:wght@800;900&display=swap">
<style>
  :root {
    --sky: #02adef;
    --ink: #000000;
    --paper: #ffffff;
    --rocket: #d47c46;
    --flame: #fde925;
  }
  html, body {
    margin: 0;
    padding: 0;
    width: 1200px;
    height: 1200px;
    overflow: hidden;
    background: var(--sky);
  }
  .tile {
    position: relative;
    width: 1200px;
    height: 1200px;
    background: var(--sky);
    overflow: hidden;
    font-family: "Montserrat", Arial, sans-serif;
  }
  .tile__shapes {
    position: absolute;
    inset: 0;
    width: 1200px;
    height: 1200px;
  }
  .shape-line {
    fill: none;
    stroke: var(--paper);
    stroke-width: 12;
    stroke-linejoin: miter;
  }
  .headline {
    position: absolute;
    left: 59px;
    top: 380px;
    margin: 0;
    width: 640px;
    line-height: 1;
  }
  .headline__small {
    display: block;
    color: var(--ink);
    font-weight: 900;
    font-size: 84px;
    letter-spacing: -1px;
    line-height: 0.95;
  }
  .headline__small--end {
    text-align: right;
    width: 622px;
    margin-top: 6px;
  }
  .headline__big {
    display: block;
    color: var(--paper);
    font-weight: 800;
    font-size: 152px;
    line-height: 0.84;
    letter-spacing: -2px;
    margin-top: 14px;
  }
</style>
</head>
<body>
  <main class="tile">
    <svg class="tile__shapes" viewBox="0 0 1200 1200" xmlns="http://www.w3.org/2000/svg">
      <polyline class="shape-line" points="-10,140 230,250 560,-10"/>
      <line class="shape-line" x1="380" y1="250" x2="900" y2="-10"/>
      <polyline class="shape-line" points="-10,1000 300,900 560,1210"/>
      <line class="shape-line" x1="-10" y1="1140" x2="640" y2="880"/>

      <defs>
        <linearGradient id="rocketTone" x1="0" y1="0" x2="0" y2="1">
          <stop offset="0" stop-color="#d47c46"/>
          <stop offset="0.62" stop-color="#d47c46"/>
          <stop offset="0.72" stop-color="#fde925"/>
          <stop offset="1" stop-color="#fde925"/>
        </linearGradient>
      </defs>
      <rect role="img" aria-label="Illustration of an orange rocket lifting off with a yellow exhaust trail"
            x="778" y="160" width="388" height="1040" rx="190" ry="190" fill="url(#rocketTone)"/>
    </svg>

    <h1 class="headline">
      <span class="headline__small">Let</span>
      <span class="headline__big">CEDAR<br>IDEAS</span>
      <span class="headline__small headline__small--end">grow</span>
    </h1>
  </main>
</body>
</html>
```